ko7ara card

the business is a virtual space for showcasing art, libraries, science, food and gifts

high end - new look - nothing fussy - clean lines - bit of colour

needs to last for ten years - at least

think the number 11 in yellow with a purple background

hope that is enough of a brief - smile

Target Market(s)

all ages

Industry/Entity Type

Business

Contact Information for Business Card

ko7ara.com
tam corley = caretaker
virtual space & larkmoor qx > nerovia

Requirements
Must have
• happy for you to choose
Nice to have
• ditto
Should not have
• anything boring - something that appeals to Gen I

```html
<!DOCTYPE html>
<html lang="en">
<head>
<meta charset="utf-8">
<title>ko7ara card</title>
<link rel="stylesheet" href="https://fonts.googleapis.com/css2?family=Open+Sans:wght@400;600;700&display=swap">
<style>
  :root {
    --page: #ecebee;
    --stripe: #e2c8e3;
    --paper: #ffffff;
    --purple: #8c3b9c;
    --lilac-box: rgba(170, 104, 184, 0.78);
    --pink-band: rgba(246, 190, 218, 0.75);
    --ink: #3a2a3c;
    --string: #1e1a1e;
    --white: #ffffff;
  }
  * { box-sizing: border-box; margin: 0; padding: 0; }
  html, body { width: 1200px; height: 900px; overflow: hidden; }
  body {
    background: var(--page);
    font-family: "Open Sans", Arial, sans-serif;
    position: relative;
  }
  .card {
    position: absolute;
    left: 280px;
    width: 640px;
    height: 384px;
    overflow: hidden;
    background: repeating-linear-gradient(90deg,
      var(--stripe) 0 22px, var(--paper) 22px 44px);
    box-shadow: 0 3px 10px rgba(0,0,0,0.18);
  }
  .card--front { top: 46px; }
  .card--back { top: 470px; }

  /* front */
  .title-band {
    position: absolute; left: 0; top: 22px; width: 100%; height: 82px;
    background: var(--purple);
    display: flex; align-items: center; justify-content: center;
  }
  .title-band__name {
    color: var(--white); font-weight: 700; font-size: 56px;
    letter-spacing: 4px; text-transform: uppercase;
  }
  .strings { position: absolute; inset: 0; width: 100%; height: 100%; }
  .artwork { position: absolute; }
  .artwork--nebula {
    left: 148px; top: 190px; width: 92px; height: 100px;
    border: 4px solid var(--white);
    background: radial-gradient(circle at 50% 50%, #f3c36a 0 10%, #d0532a 22%, #4a2c48 38%, #0c0c14 62%);
    box-shadow: 2px 3px 6px rgba(0,0,0,0.3);
  }
  .artwork--portrait {
    left: 290px; top: 160px; width: 106px; height: 152px;
    border: 6px solid #b7772b;
    background: linear-gradient(160deg, #e8c9a0, #c98a4f 50%, #8f5b36);
    box-shadow: 2px 3px 6px rgba(0,0,0,0.3);
  }
  .artwork--glass {
    left: 420px; top: 162px; width: 84px; height: 120px;
    border: 5px solid #c9c9cc;
    background: linear-gradient(140deg, #2f7fc4, #3fa36e 45%, #1d3e8c 75%, #d45a3a);
    box-shadow: 2px 3px 6px rgba(0,0,0,0.3);
  }

  /* back */
  .sign {
    position: absolute; left: 92px; top: 126px; width: 176px; height: 70px;
    background: var(--purple);
    transform: rotate(-6deg);
    display: flex; align-items: center; justify-content: center;
  }
  .sign__name { color: var(--white); font-weight: 700; font-size: 34px; }
  .contact {
    position: absolute; left: 360px; top: 100px; width: 240px; height: 112px;
    background: var(--lilac-box); color: var(--white);
    padding: 6px 10px;
  }
  .contact__name { font-size: 23px; font-weight: 400; line-height: 1.2; margin-bottom: 10px; }
  .contact__line { font-size: 15px; line-height: 1.15; }
  .motto {
    position: absolute; left: 70px; top: 248px; width: 520px; height: 62px;
    background: var(--pink-band); color: var(--ink);
    font-size: 12.5px; line-height: 1.35; text-align: center;
    display: flex; flex-direction: column; justify-content: center;
  }
  .web {
    position: absolute; left: 180px; bottom: 0; width: 260px; height: 32px;
    background: var(--purple); border-radius: 16px 16px 0 0;
    color: var(--white); font-weight: 700; font-size: 16px;
    display: flex; align-items: center; justify-content: center;
  }
</style>
</head>
<body>
  <section class="card card--front">
    <div class="title-band"><span class="title-band__name">ko7ara</span></div>
    <svg class="strings" viewBox="0 0 640 384">
      <g stroke="var(--string)" stroke-width="2" fill="none">
        <polyline points="150,194 194,136 238,194"/>
        <polyline points="292,164 343,112 394,164"/>
        <polyline points="422,166 462,116 502,166"/>
      </g>
      <g fill="var(--string)">
        <circle cx="194" cy="136" r="4"/>
        <circle cx="343" cy="112" r="4"/>
        <circle cx="462" cy="116" r="4"/>
      </g>
    </svg>
    <div class="artwork artwork--nebula" role="img" aria-label="Space photograph of a glowing orange nebula"></div>
    <div class="artwork artwork--portrait" role="img" aria-label="Painted portrait artwork in warm tones"></div>
    <div class="artwork artwork--glass" role="img" aria-label="Colourful mosaic style artwork"></div>
  </section>

  <section class="card card--back">
    <svg class="strings" viewBox="0 0 640 384">
      <g stroke="var(--string)" stroke-width="2" fill="none">
        <line x1="130" y1="0" x2="104" y2="132"/>
        <line x1="200" y1="0" x2="254" y2="114"/>
      </g>
    </svg>
    <div class="sign"><span class="sign__name">ko7ara</span></div>
    <div class="contact">
      <p class="contact__name">tam corley</p>
      <p class="contact__line">caretaker virtual space</p>
      <p class="contact__line">larkmoor qx</p>
      <p class="contact__line">nerovia</p>
    </div>
    <div class="motto">
      <p>most things ... start small ideas, babies ... even rivers</p>
      <p>so watch ... this grow think large ... love small</p>
    </div>
    <div class="web">ko7ara.com</div>
  </section>
</body>
</html>
```